A Referral Pad for a Specialist Surgeon to give to referring GPs

A referral pad allows general practitioners to easily refer patients to me by quickly filling in a form on a small pad that I provide them.

A two sided referral pad themed appropriately. Theming and designing the pad should be based on the general design/logo/imagery/colours etc. from my website www.marcuspellwright.com.au. I have a logo uploaded that should be used somewhere. I have also upload a headshot of myself which might or might not be used. Other choice of imagery and design features is up to the designer.

In terms of size of the pad I’m not quite sure what is best and will leave it up to the designers.

MORE DETAILED INFORMATION IS PROVIDED IN THE UPLOADED WORD FILE

Target Market(s)

General Practitioners referring to me

Industry/Entity Type

Healthcare

Contact Information for Business Card

A business card themed as per the referral pad design as as per general look and imagery found on www.marcuspellwright.com.au

Requirements
Must have
• Referral pad details found in uploaded Word document
Nice to have
Should not have

```html
<!DOCTYPE html>
<html lang="en">
<head>
<meta charset="utf-8">
<title>Patient Referral – Marcus Pellwright</title>
<link rel="stylesheet" href="https://fonts.googleapis.com/css2?family=Lato:wght@400&family=Sorts+Mill+Goudy&display=swap">
<style>
  :root {
    --teal: #1a9488;
    --teal-band: #1f9387;
    --ink: #555a5c;
    --rule: #6b6f71;
    --panel: #fbfbfb;
    --heading-grey: #6d6f70;
  }
  * { margin: 0; padding: 0; box-sizing: border-box; }
  html, body { width: 887px; height: 1200px; overflow: hidden; background: #fff; }
  body { position: relative; font-family: "Lato", sans-serif; color: var(--ink); }
  .abs { position: absolute; white-space: nowrap; }
  .serif { font-family: "Sorts Mill Goudy", serif; }

  .brand-mark { left: 216px; top: 78px; width: 74px; height: 74px; border-radius: 50%; background: var(--teal); }
  .brand-name { left: 307px; top: 89px; font-family: "Sorts Mill Goudy", serif; font-size: 38px; color: var(--teal); letter-spacing: 0.5px; }
  .brand-tagline { left: 308px; top: 130px; font-family: "Sorts Mill Goudy", serif; font-size: 12.5px; color: #7a7d7f; letter-spacing: 2.6px; text-transform: uppercase; }

  .form-title { left: 54px; top: 228px; font-size: 32px; color: var(--teal); }
  .label { font-size: 15.5px; color: var(--ink); }
  .label-lg { font-size: 19px; color: #6a6e70; }
  .fill-line { position: absolute; height: 0; border-bottom: 1px solid var(--rule); }

  .section-title { font-family: "Sorts Mill Goudy", serif; font-size: 21px; color: var(--teal); }
  .panel { position: absolute; background: var(--panel); }

  .check { position: absolute; width: 21px; height: 21px; border: 1.3px solid #3f4446; background: #fff; }

  .footnote { left: 72px; top: 892px; font-size: 14.5px; color: var(--teal); }

  .contact-heading { left: 0; width: 887px; top: 1046px; text-align: center; font-family: "Sorts Mill Goudy", serif; font-weight: 400; font-size: 27px; color: var(--heading-grey); letter-spacing: -0.3px; -webkit-text-stroke: 0.5px var(--heading-grey); }
  .contact-band { position: absolute; left: 0; top: 1093px; width: 887px; height: 48px; background: var(--teal-band); }
  .contact-band span { position: absolute; top: 14px; font-size: 15.5px; color: #fff; white-space: nowrap; }
</style>
</head>
<body>
  <header>
    <div class="abs brand-mark" aria-hidden="true"></div>
    <div class="abs brand-name">MARCUS PELLWRIGHT</div>
    <div class="abs brand-tagline">General, Upper GI &amp; Bariatric Surgeon</div>
  </header>

  <h1 class="abs serif form-title" style="font-weight:400">Patient Referral</h1>
  <span class="abs label-lg" style="left:528px;top:239px">Referral Date</span>
  <span class="fill-line" style="left:660px;top:256px;width:164px"></span>

  <section class="patient-details">
    <span class="abs label" style="left:52px;top:307px">Patient name</span>
    <span class="fill-line" style="left:157px;top:322px;width:224px"></span>
    <span class="abs label" style="left:392px;top:307px">Date of birth</span>
    <span class="fill-line" style="left:490px;top:322px;width:148px"></span>
    <span class="abs label" style="left:645px;top:307px">Gender</span>
    <span class="fill-line" style="left:701px;top:322px;width:123px"></span>

    <span class="abs label" style="left:52px;top:339px">Phone</span>
    <span class="fill-line" style="left:106px;top:354px;width:221px"></span>
    <span class="abs label" style="left:342px;top:339px">Email</span>
    <span class="fill-line" style="left:390px;top:354px;width:436px"></span>
  </section>

  <div class="panel" style="left:46px;top:374px;width:784px;height:125px"></div>
  <h2 class="abs section-title" style="left:54px;top:384px;font-weight:400">Medical History/Comments</h2>

  <h2 class="abs section-title" style="left:52px;top:518px;font-weight:400">Consulting Locations</h2>
  <span class="abs label" style="left:75px;top:558px">1. Melbourne:&nbsp; Harlow St CBD, Box Hill, Rowville</span>
  <span class="check" style="left:441px;top:556px"></span>
  <span class="abs label" style="left:473px;top:558px">2. Regional:&nbsp; Bendigo, Kyneton, Moe, Foster</span>
  <span class="check" style="left:804px;top:557px;width:19px;height:20px"></span>

  <h2 class="abs section-title" style="left:51px;top:586px;font-weight:400">Procedure Choice</h2>
  <span class="abs label" style="left:72px;top:624px">1. Bariatric Surgery (see over for details &amp; eligibility)</span>

  <span class="abs label" style="left:92px;top:661px">a. Patient weight :</span>
  <span class="fill-line" style="left:246px;top:674px;width:83px"></span>
  <span class="abs label" style="left:358px;top:661px">b. Patient BMI :</span>
  <span class="fill-line" style="left:491px;top:674px;width:99px"></span>
  <span class="abs label" style="left:614px;top:661px">c. Diabetic :&nbsp; Yes</span>
  <span class="check" style="left:744px;top:658px;width:20px;height:20px"></span>
  <span class="abs label" style="left:774px;top:661px">No</span>
  <span class="check" style="left:803px;top:658px;width:20px;height:20px"></span>

  <ol class="procedure-list">
    <li class="abs label" style="left:72px;top:695px;list-style:none">2. Abdominoplasty or Arm Reduction after weight loss</li>
    <li class="abs label" style="left:72px;top:727px;list-style:none">3. Antireflux/Hiatus Hernia Surgery</li>
    <li class="abs label" style="left:72px;top:761px;list-style:none">4. Gallbladder</li>
    <li class="abs label" style="left:72px;top:790px;list-style:none">5. Hernia</li>
    <li class="abs label" style="left:72px;top:824px;list-style:none">6. Endoscopy</li>
    <li class="abs label" style="left:72px;top:857px;list-style:none">7. Other general surgery*</li>
  </ol>
  <span class="check" style="left:569px;top:695px"></span>
  <span class="check" style="left:569px;top:727px"></span>
  <span class="check" style="left:569px;top:760px"></span>
  <span class="check" style="left:569px;top:794px"></span>
  <span class="check" style="left:569px;top:826px"></span>
  <span class="check" style="left:569px;top:858px"></span>

  <p class="abs footnote">*Includes skin, lumps &amp; bumps, peri-anal/haemorrhoids,varicose veins, carpal tunnel.</p>

  <h2 class="abs section-title" style="left:54px;top:961px;font-weight:400">General practitioner details/stamp</h2>
  <div class="panel" style="left:380px;top:950px;width:446px;height:52px"></div>

  <h2 class="abs contact-heading">Clinic Contact Details</h2>
  <footer class="contact-band">
    <span style="left:46px">Fax (03) 9555 0148</span>
    <span style="left:214px">All appointments (03) 9555 0162</span>
    <span style="left:486px">Email: info@pellwrightsurgical.com.au</span>
  </footer>
</body>
</html>
```